Brightmoor Surface Index

I have a current web site that it looking quite aged and it needs a new lease of life. This is a Graffiti Management Website so is all about data processing and management of information. I want a html 5 view on any platform design. clean crisp and new. I have provided some screen shots of my current site.

Target Market(s)

The Target Market will be local government. most users will not be heavy pc users

Industry/Entity Type

Management

Font styles to use
Sans Serif
Other font styles liked:
• web font like calibri

Colors

Designer to choose colors to be used in the design.

Requirements
Must have
• Must have menus similar to attachments

```html
<!DOCTYPE html>
<html lang="en">
<head>
<meta charset="utf-8">
<title>Brightmoor Surface Index</title>
<link href="https://fonts.googleapis.com/css2?family=Open+Sans:wght@400;600;700;800&display=swap" rel="stylesheet">
<style>
:root{
  --teal:#22b59a;
  --teal-dark:#179a82;
  --teal-card:rgba(34,181,154,.88);
  --ink:#2d2d2d;
  --text:#555;
  --white:#fff;
  --footer:#262a2b;
  --line:rgba(255,255,255,.45);
}
*{margin:0;padding:0;box-sizing:border-box}
html,body{width:1200px;height:2456px;overflow:hidden}
body{font-family:"Open Sans",Arial,sans-serif;color:var(--text);background:var(--white);position:relative}
section,header,footer{position:absolute;left:0;width:1200px}

/* hero */
.hero{top:0;height:500px;background:linear-gradient(160deg,#4b5a66 0%,#6d6f72 35%,#8a5a3e 60%,#3f4c57 100%)}
.hero-photo{position:absolute;inset:0}
.hero-shade{position:absolute;inset:0;background:linear-gradient(180deg,rgba(0,0,0,.45),rgba(0,0,0,.25) 40%,rgba(0,0,0,.45))}
.topbar{position:absolute;top:0;left:0;width:1200px;height:78px;border-bottom:1px solid rgba(255,255,255,.15);background:rgba(0,0,0,.35)}
.brand{position:absolute;left:22px;top:14px;color:var(--white)}
.brand-name{font-size:30px;font-weight:800;letter-spacing:1px;line-height:34px}
.brand-sub{font-size:9px;font-weight:600;letter-spacing:1.5px;opacity:.85}
.nav{position:absolute;right:22px;top:30px;display:flex;gap:6px}
.nav a{color:var(--white);text-decoration:none;font-size:13px;font-weight:700;padding:7px 12px;letter-spacing:.5px}
.nav a.active{background:var(--teal)}
.hero-copy{position:absolute;top:300px;width:1200px;text-align:center;color:var(--white)}
.hero-copy h1{font-size:46px;line-height:52px;font-weight:800;letter-spacing:1px}
.hero-copy p{font-size:12px;font-weight:600;letter-spacing:1px;margin-top:10px}
.dots{position:absolute;top:456px;width:1200px;display:flex;justify-content:center;gap:10px}
.dots span{width:11px;height:11px;border-radius:50%;background:var(--teal)}
.dots span.on{background:var(--white)}

/* titles */
.section-title{font-size:32px;font-weight:700;color:var(--ink);text-align:center}
.rule{width:1060px;height:1px;background:#e1e1e1;margin:18px auto 26px}

/* welcome */
.welcome{top:500px;height:530px;padding-top:62px;text-align:center}
.welcome p{font-size:14px;line-height:20px;margin-bottom:16px;color:#444}

/* products */
.products{top:1030px;height:450px;background:linear-gradient(135deg,#5a6a78 0%,#8c7f6c 30%,#b6885a 55%,#6b7c8c 80%,#495864 100%)}
.products .shade{position:absolute;inset:0;background:rgba(20,30,35,.45)}
.products .section-title{position:relative;color:var(--white);padding-top:40px}
.products .rule{position:relative;background:rgba(255,255,255,.3)}
.cards{position:absolute;top:140px;left:0;width:1200px;display:flex;justify-content:center;gap:48px}
.card{width:208px;height:272px;background:var(--teal-card);text-align:center;color:var(--white);padding:26px 18px}
.card svg{display:block;margin:0 auto 16px}
.card h3{font-size:15px;font-weight:700;letter-spacing:.5px}
.card p{font-size:11px;line-height:15px;margin:10px 0 26px;opacity:.95}
.btn{display:inline-block;font-size:10px;font-weight:700;letter-spacing:1px;color:var(--white);border:1px solid rgba(255,255,255,.6);padding:6px 20px;background:var(--teal-dark)}
.arrow{position:absolute;top:270px}
.arrow.left{left:14px}.arrow.right{right:14px}

/* legislation */
.legislation{top:1480px;height:262px;padding-top:50px;text-align:center}
.legislation p{font-size:14px;line-height:24px;color:#444}
.legislation .btn{margin-top:18px;border:none;background:var(--teal);padding:8px 18px}

/* benefits */
.benefits{top:1742px;height:622px;background:var(--teal);color:var(--white)}
.benefits .section-title{color:var(--white);padding-top:68px}
.benefits .rule{background:var(--line)}
.grid{position:absolute;top:190px;left:100px;width:1000px;height:390px}
.grid .vline{position:absolute;left:500px;top:0;width:1px;height:390px;background:var(--line)}
.grid .hline{position:absolute;top:195px;left:0;width:1000px;height:1px;background:var(--line)}
.benefit{position:absolute;width:450px;display:flex;gap:22px}
.benefit svg{flex:none}
.benefit h4{font-size:17px;font-weight:700;letter-spacing:.5px;margin-bottom:10px}
.benefit p{font-size:12px;line-height:18px;opacity:.95}
.b1{left:10px;top:20px}.b2{left:530px;top:20px}.b3{left:10px;top:225px}.b4{left:530px;top:225px}

/* footer */
.footer{top:2364px;height:92px;background:var(--footer);color:#bfc4c5;font-size:11px}
.footer .copy{position:absolute;left:22px;top:70px}
.footer .addr{position:absolute;left:530px;top:22px;display:flex;gap:12px;line-height:16px}
.footer .mail{position:absolute;right:22px;top:22px;text-align:right;line-height:16px}
</style>
</head>
<body>

<header class="hero">
  <div class="hero-photo" role="img" aria-label="Photo of a worker cleaning graffiti from a wall"></div>
  <div class="hero-shade"></div>
  <div class="topbar">
    <div class="brand">
      <div class="brand-name">BRIGHTMOOR</div>
      <div class="brand-sub">BRIGHTMOOR SURFACE INDEX</div>
    </div>
    <nav class="nav">
      <a class="active" href="#">HOME</a><a href="#">PRODUCTS</a><a href="#">REPORTS</a><a href="#">BENEFITS</a><a href="#">LEGISLATION</a><a href="#">CONTACT US</a><a href="#">LOG IN</a>
    </nav>
  </div>
  <div class="hero-copy">
    <h1>HELPING YOU CLEAN<br>UP YOUR COMMUNITY</h1>
    <p>OUR WORK IS DEDICATED TO THE PROSPERITY OF OUR CLIENTS</p>
  </div>
  <div class="dots"><span></span><span class="on"></span><span></span></div>
</header>

<section class="welcome">
  <h2 class="section-title">Welcome</h2>
  <div class="rule"></div>
  <p>Brightmoor is an Online Database System to Manage Graffiti in your area or Your Properties.</p>
  <p>Brightmoor allows you to Register, Track, Report and Archive Graffiti Jobs with Photographic Records.</p>
  <p>Brightmoor records both Estimated and Actual hours and costs for each job, enabling you to track the effectiveness of Anti Graffiti policy.</p>
  <p>Brightmoor allows sharing of Critical Graffiti Tag and Photography Data between its subscribers, assisting with tracking down Serial Graffiti Offenders.</p>
  <p>Brightmoor has a Statistical and Comparison Reporting Systems to allow its subscribers to graphically report and compare their Graffiti Data.</p>
</section>

<section class="products">
  <div class="products-photo" role="img" aria-label="Background photo of a colourful graffiti covered wall" style="position:absolute;inset:0"></div>
  <div class="shade"></div>
  <h2 class="section-title">Our Products</h2>
  <div class="rule"></div>
  <svg class="arrow left" width="14" height="28" viewBox="0 0 14 28"><path d="M12 2 2 14l10 12" fill="none" stroke="#fff" stroke-width="2"/></svg>
  <svg class="arrow right" width="14" height="28" viewBox="0 0 14 28"><path d="M2 2l10 12L2 26" fill="none" stroke="#fff" stroke-width="2"/></svg>
  <div class="cards">
    <div class="card">
      <svg width="48" height="48" viewBox="0 0 48 48"><rect x="10" y="6" width="28" height="36" rx="2" fill="none" stroke="#fff" stroke-width="3"/><path d="M16 16h16M16 24h16M16 32h10" stroke="#fff" stroke-width="3"/></svg>
      <h3>GRAFFITI REGISTER</h3>
      <p>Brightmoor provides a Personal Register of Vandalism and Graffiti.</p>
      <span class="btn">MORE</span>
    </div>
    <div class="card">
      <svg width="48" height="48" viewBox="0 0 48 48"><rect x="6" y="14" width="36" height="24" rx="3" fill="none" stroke="#fff" stroke-width="3"/><circle cx="24" cy="26" r="7" fill="none" stroke="#fff" stroke-width="3"/><rect x="17" y="9" width="14" height="5" fill="#fff"/></svg>
      <h3>GRAFFITI PHOTOS</h3>
      <p>Brightmoor allows its subscribers to add Digital Photographs to the Graffiti Jobs.</p>
      <span class="btn">MORE</span>
    </div>
    <div class="card">
      <svg width="48" height="48" viewBox="0 0 48 48"><ellipse cx="24" cy="12" rx="14" ry="5" fill="none" stroke="#fff" stroke-width="3"/><path d="M10 12v24c0 3 6 5 14 5s14-2 14-5V12M10 24c0 3 6 5 14 5s14-2 14-5" fill="none" stroke="#fff" stroke-width="3"/></svg>
      <h3>SEARCHABLE DATABASE</h3>
      <p>Brightmoor allows you to search your own records in limited data from others subscribers.</p>
      <span class="btn">MORE</span>
    </div>
  </div>
</section>

<section class="legislation">
  <h2 class="section-title">Legislation</h2>
  <div class="rule"></div>
  <p>Brightmoor can assist with the possible prosecution of offenders with records of previous tags inside your local area<br>as well as any other subscribers tags. This will effectively show the extent of the offenders activities.</p>
  <span class="btn">VIEW MORE</span>
</section>

<section class="benefits">
  <h2 class="section-title">Our Benefits</h2>
  <div class="rule"></div>
  <div class="grid">
    <div class="vline"></div><div class="hline"></div>
    <div class="benefit b1">
      <svg width="44" height="44" viewBox="0 0 44 44"><ellipse cx="22" cy="12" rx="14" ry="5" fill="#fff"/><path d="M8 18c0 3 6 5 14 5s14-2 14-5M8 25c0 3 6 5 14 5s14-2 14-5M8 32c0 3 6 5 14 5s14-2 14-5" fill="none" stroke="#fff" stroke-width="3"/></svg>
      <div><h4>COST EFFECTIVE</h4><p>Brightmoor allows you to track the cost and effectiveness of your Graffiti Removal. Compare the estimate &amp; actual costs for External Contractors against in-house removal.</p></div>
    </div>
    <div class="benefit b2">
      <svg width="44" height="44" viewBox="0 0 44 44"><rect x="4" y="12" width="36" height="24" rx="3" fill="none" stroke="#fff" stroke-width="3"/><circle cx="22" cy="24" r="7" fill="#fff"/><rect x="15" y="7" width="14" height="5" fill="#fff"/></svg>
      <div><h4>PHOTOGRAPHIC RECORDS</h4><p>Store any photographic records of New, Existing and Completed Graffiti Jobs. Archive all completed works including photos of "cleaned" areas.</p></div>
    </div>
    <div class="benefit b3">
      <svg width="44" height="44" viewBox="0 0 44 44"><circle cx="22" cy="14" r="8" fill="#fff"/><path d="M6 40c0-9 7-15 16-15s16 6 16 15z" fill="#fff"/></svg>
      <div><h4>ASSIST PROSECUTION</h4><p>Brightmoor can assist with the possible prosecution of offenders with records of previous tags inside your local area as well as any other subscribers tags. This will effectively show the extent of the offenders activities.</p></div>
    </div>
    <div class="benefit b4">
      <svg width="44" height="44" viewBox="0 0 44 44"><path d="M13 20v-6a9 9 0 0 1 18 0v6" fill="none" stroke="#fff" stroke-width="3"/><rect x="8" y="20" width="28" height="20" rx="3" fill="#fff"/></svg>
      <div><h4>ACCESS AND SECURITY</h4><p>You can access your data from any PC around the world connected to the internet. You can give access to your trusted contractors to update your data for you. You can also set levels of access for your staff logins.</p></div>
    </div>
  </div>
</section>

<footer class="footer">
  <div class="copy">copyright 2024 Brightmoor all rights reserved</div>
  <div class="addr">
    <svg width="16" height="22" viewBox="0 0 16 22"><path d="M8 1a7 7 0 0 0-7 7c0 5 7 13 7 13s7-8 7-13a7 7 0 0 0-7-7z" fill="var(--teal)"/><circle cx="8" cy="8" r="2.5" fill="var(--footer)"/></svg>
    <div>Brightmoor Surface Index<br>PO Box 118, Eastfield 4021<br>Ph (07) 5550 0148</div>
  </div>
  <div class="mail">Mail: hello@brightmoor-index.example<br>Web: brightmoor-index.example</div>
</footer>

</body>
</html>
```